Thistlecrows--Wine Bottle Label for Marlow Thicket

We need a design for a wine bottle labels for 2 custom wines that a local winery is producing for our hunting lodge, Marlow Thicket. The lodge restaurant is called "Thistlecrows", so we'd like to use that as the theme for the label picture. The thought is that we'd use the same design but with different colors for the two types--Red Table Wine and White Table Wine. You can check out our website at www.marlowthicket-demo.com for inspiration. Since there are many regulations on what goes on the label bottled alcohol in the US, we are just looking for the artwork to be used on the label.

Industry/Entity Type

Hunting

Font styles to use
Decorative
Script

Requirements
Must have
• Thistlecrows (as in male US pheasants) should be included in the design.
Nice to have
• It would be nice to have somewhat of an abstract version of a Rooster Pheasant in the design. We would like to see the same design in 2 different color palettes.

```html
<!DOCTYPE html>
<html lang="en">
<head>
<meta charset="utf-8">
<title>Marlow Thicket Wine Label</title>
<link rel="stylesheet" href="https://fonts.googleapis.com/css2?family=Cinzel:wght@400;500&family=Cormorant+Garamond:wght@500&display=swap">
<style>
  :root {
    --backdrop: #2a2624;
    --label-paper: #f4f2ee;
    --wine-red: #a3232a;
    --ink-soft: #6e3a34;
    --art-light: #e6e1da;
    --art-mid: #bdaea2;
    --art-deep: #8a5a4c;
  }
  * { margin: 0; padding: 0; box-sizing: border-box; }
  html, body {
    width: 1200px;
    height: 1000px;
    overflow: hidden;
    background: var(--backdrop);
  }
  .canvas {
    position: relative;
    width: 1200px;
    height: 1000px;
  }
  .wine-label {
    position: absolute;
    left: 370px;
    top: 40px;
    width: 460px;
    height: 920px;
    background: var(--label-paper);
    border-radius: 18px;
    text-align: center;
    color: var(--wine-red);
  }
  .brand-mark {
    position: absolute;
    top: 70px;
    left: 0;
    right: 0;
    display: flex;
    flex-direction: column;
    align-items: center;
    gap: 22px;
  }
  .brand-dot {
    width: 54px;
    height: 54px;
    border-radius: 50%;
    background: var(--wine-red);
  }
  .brand-name {
    font-family: "Cinzel", serif;
    font-weight: 500;
    font-size: 26px;
    letter-spacing: 1px;
    color: var(--wine-red);
    padding-bottom: 6px;
    border-bottom: 2px solid var(--wine-red);
  }
  .pheasant-art {
    position: absolute;
    left: 40px;
    top: 250px;
    width: 380px;
    height: 460px;
    border-radius: 50%;
    background: radial-gradient(ellipse at 50% 45%, var(--art-mid) 0%, var(--art-light) 55%, var(--label-paper) 78%);
  }
  .pheasant-art::after {
    content: "";
    position: absolute;
    left: 110px;
    top: 40px;
    width: 170px;
    height: 380px;
    border-radius: 48% 48% 40% 40%;
    background: linear-gradient(180deg, var(--art-deep) 0%, var(--ink-soft) 60%, var(--art-mid) 100%);
    opacity: 0.55;
  }
  .wine-title {
    position: absolute;
    top: 460px;
    left: 0;
    right: 0;
    font-family: "Cinzel", serif;
    font-weight: 400;
    font-size: 60px;
    line-height: 1.05;
    letter-spacing: -1px;
    color: var(--wine-red);
  }
  .varietal {
    position: absolute;
    top: 770px;
    left: 0;
    right: 0;
    font-family: "Cormorant Garamond", serif;
    font-weight: 500;
    font-size: 34px;
    color: var(--ink-soft);
  }
  .vintage {
    position: absolute;
    top: 830px;
    left: 0;
    right: 0;
    font-family: "Cormorant Garamond", serif;
    font-weight: 500;
    font-size: 28px;
    color: var(--ink-soft);
  }
</style>
</head>
<body>
  <main class="canvas">
    <section class="wine-label">
      <div class="brand-mark">
        <span class="brand-dot"></span>
        <span class="brand-name">Thistlecrows</span>
      </div>
      <div class="pheasant-art" role="img" aria-label="Engraved illustration of a standing pheasant"></div>
      <h1 class="wine-title">MARLOW<br>THICKET</h1>
      <p class="varietal">Cabernet Sauvignon</p>
      <p class="vintage">2016</p>
    </section>
  </main>
</body>
</html>
```